Pine Ridge Golf New Location Postcard

I need a postcard announcing our new location. It is a indoor golf training facility that offers award winner instruction, state-of-the-art technology, and custom club fitting. Whether you are a beginner, an aspiring athlete, or an amateur, Pine Ridge Golf offers personalized programs to help take your game to the next level. Call now to schedule your free tour or to sign up. Limited memberships available.
I would like somewhere are on postcard to say Don't put away your clubs just yet! The course may be closed but Pine Ridge Golf's new indoor location is open!
Training

```html
<!DOCTYPE html>
<html lang="en">
<head>
<meta charset="utf-8">
<title>Pine Ridge Golf – New Location Postcard</title>
<link href="https://fonts.googleapis.com/css2?family=Open+Sans:wght@300;400;600;700;800&family=Anton&display=swap" rel="stylesheet">
<style>
  :root{
    --page:#ecebe8;
    --green-dark:#3a6619;
    --green:#5f9130;
    --red:#e2393f;
    --red-dark:#c92a30;
    --ink:#242424;
    --band:#2b2b2b;
    --silver:#c9c9c9;
    --white:#ffffff;
    --grey-text:#5a5a5a;
  }
  *{box-sizing:border-box;margin:0;padding:0}
  html,body{width:850px;height:1200px;overflow:hidden}
  body{background:var(--page);font-family:"Open Sans",Arial,sans-serif;position:relative}
  .postcard{position:absolute;left:85px;width:680px;height:522px;overflow:hidden;
    background:var(--white);box-shadow:0 4px 14px rgba(0,0,0,.25)}
  .postcard--front{top:52px}
  .postcard--back{top:626px}
  .postcard svg.backdrop{position:absolute;inset:0}
  .abs{position:absolute}

  /* brand name block */
  .brand{position:absolute}
  .brand__name{font-weight:600;color:var(--ink);line-height:1;white-space:nowrap}
  .brand__tag{color:var(--grey-text);letter-spacing:1.2px;white-space:nowrap;text-transform:uppercase}
  .front .brand{left:420px;top:26px}
  .front .brand__name{font-size:26px}
  .front .brand__tag{font-size:9.5px;margin-top:7px}
  .back .brand{left:360px;top:28px}
  .back .brand__name{font-size:21px}
  .back .brand__tag{font-size:8px;margin-top:5px}

  /* front headline */
  .headline{left:348px;top:110px;width:322px;color:var(--white);text-transform:uppercase;line-height:1.12}
  .headline span{display:block;white-space:nowrap}
  .headline .l1{font-size:14px;font-weight:400}
  .headline .l2{font-size:18.5px;font-weight:400}
  .headline b{font-weight:800}
  .headline .l3{font-size:17px;font-weight:800;color:var(--red)}
  .headline .l4{font-size:27px;font-weight:800}

  .offer-pill{left:348px;top:232px;width:174px;height:32px;border-radius:7px;
    background:linear-gradient(#4a4a4a,#1e1e1e);color:var(--white);font-weight:700;font-size:22px;
    display:flex;align-items:center;justify-content:center;letter-spacing:.5px}
  .offer-list{left:348px;top:277px;list-style:none;color:var(--white)}
  .offer-list li{display:flex;align-items:center;font-weight:600;font-size:15px;height:25.5px}
  .offer-list svg{width:14px;height:12px;margin-right:19px}
  .intro{left:348px;top:363px;width:324px;color:var(--white);font-size:12.4px;line-height:1.55}

  .front-contact{color:var(--white);font-size:10.5px;display:flex;align-items:flex-start}
  .front-contact svg{flex:none;margin-right:8px}
  .address{left:320px;top:482px;line-height:1.5}
  .phone-line{left:512px;top:471px;font-size:17px;font-weight:700;align-items:center}
  .web-line{left:512px;top:496px;font-size:11.5px;align-items:center}
  .web-line em,.web-back em{font-style:normal;color:var(--red)}

  /* back */
  .call-sign{left:14px;top:33px;width:248px;height:155px;border-radius:9px;border:3px solid #d8d8d8;
    background:linear-gradient(#ef6065,var(--red) 45%,var(--red-dark));overflow:hidden;color:var(--white);text-align:center}
  .call-sign__title{font-family:"Anton",Impact,sans-serif;font-size:31px;color:var(--ink);line-height:1;margin-top:10px;letter-spacing:.5px}
  .call-sign__sub{font-size:12.5px;font-weight:600;margin:4px auto 0;width:170px;border-top:1px solid rgba(255,255,255,.8);border-bottom:1px solid rgba(255,255,255,.8);padding:1px 0}
  .call-sign__phone{font-size:21px;font-weight:700;margin-top:5px;display:flex;align-items:center;justify-content:center;gap:10px}
  .call-sign__mail{font-size:13.5px;margin-top:1px;display:flex;align-items:center;justify-content:center;gap:10px}
  .call-sign__foot{position:absolute;left:0;right:0;bottom:0;height:27px;background:#1c1c1c;font-size:11px;font-weight:700;
    display:flex;align-items:center;justify-content:center;letter-spacing:.3px}
  .sign-cord{top:0;width:1px;height:42px;background:#cfcfcf}
  .location-map{left:19px;top:208px;width:309px;height:174px;border-radius:8px;
    background:linear-gradient(135deg,#f1efe9,#e3e3de);box-shadow:0 2px 6px rgba(0,0,0,.4)}
  .web-back{left:80px;top:410px;font-size:13px;color:var(--ink);display:flex;align-items:center;gap:8px}
  .stamp-box{left:569px;top:18px;width:91px;height:90px;border:1px solid #333}
  .address-line{left:432px;width:228px;height:1px;background:#333}
</style>
</head>
<body>

<!-- FRONT -->
<section class="postcard postcard--front front">
  <svg class="backdrop" width="680" height="522" viewBox="0 0 680 522">
    <defs>
      <linearGradient id="indoorGreen" x1="0" y1="0" x2="0" y2="1">
        <stop offset="0" stop-color="#8fc46a"/>
        <stop offset=".45" stop-color="var(--green)"/>
        <stop offset="1" stop-color="var(--green-dark)"/>
      </linearGradient>
      <linearGradient id="outdoorScene" x1="0" y1="0" x2="0" y2="1">
        <stop offset="0" stop-color="#eef0de"/>
        <stop offset=".5" stop-color="#9fb279"/>
        <stop offset=".75" stop-color="#5e7e3c"/>
        <stop offset="1" stop-color="#7ea54a"/>
      </linearGradient>
      <linearGradient id="silver" x1="0" y1="0" x2="1" y2="0">
        <stop offset="0" stop-color="#9a9a9a"/><stop offset=".5" stop-color="#f4f4f4"/><stop offset="1" stop-color="#a8a8a8"/>
      </linearGradient>
    </defs>
    <rect width="680" height="522" fill="url(#indoorGreen)" role="img" aria-label="Indoor golf training bay with putting green and simulator screen"/>
    <rect x="300" y="0" width="380" height="84" fill="rgba(255,255,255,.86)"/>
    <path d="M232 0 C300 20 345 80 330 150 C318 230 230 290 190 334 C240 360 300 400 306 470 L290 522 L0 522 L0 0 Z"
          fill="none" stroke="url(#silver)" stroke-width="14"/>
    <path d="M232 0 C300 20 345 80 330 150 C318 230 230 290 190 334 C240 360 300 400 306 470 L290 522 L0 522 L0 0 Z"
          fill="url(#outdoorScene)" role="img" aria-label="Golfer finishing a swing on an outdoor course"/>
    <polygon points="300,470 522,470 537,453 680,453 680,522 290,522" fill="var(--band)"/>
    <polyline points="300,468 521,468 536,451 680,451" fill="none" stroke="var(--silver)" stroke-width="3"/>
  </svg>

  <div class="brand">
    <div class="brand__name">Pine Ridge Golf</div>
    <div class="brand__tag">Indoor golf training center</div>
  </div>

  <h1 class="abs headline">
    <span class="l1">Don't put away <b>your clubs just yet!</b></span>
    <span class="l2"><b>The course may</b> be closed but</span>
    <span class="l3">Pine Ridge Golf's new indoor</span>
    <span class="l4">Location is open!</span>
  </h1>

  <div class="abs offer-pill">WE OFFER</div>
  <ul class="abs offer-list">
    <li><svg viewBox="0 0 14 12"><path d="M1 6.5 L5 10.5 L13 1" fill="none" stroke="#fff" stroke-width="1.6"/></svg>Award winning instruction</li>
    <li><svg viewBox="0 0 14 12"><path d="M1 6.5 L5 10.5 L13 1" fill="none" stroke="#fff" stroke-width="1.6"/></svg>State-of-the-art technology</li>
    <li><svg viewBox="0 0 14 12"><path d="M1 6.5 L5 10.5 L13 1" fill="none" stroke="#fff" stroke-width="1.6"/></svg>Custom club fitting</li>
  </ul>
  <p class="abs intro">Whether you are a beginner, an aspiring athlete, or an amateur, Pine Ridge Golf offers personalized programs to help take your game to the next level.</p>

  <div class="abs front-contact address">
    <svg width="16" height="16" viewBox="0 0 16 16"><circle cx="8" cy="8" r="7" fill="none" stroke="#fff"/><path d="M8 3.5a2.8 2.8 0 0 0-2.8 2.8C5.2 8.5 8 12 8 12s2.8-3.5 2.8-5.7A2.8 2.8 0 0 0 8 3.5z" fill="var(--red)"/></svg>
    <div>1480 Birchwood Ave.<br>Unit B4 Fairhaven, OH 45002</div>
  </div>
  <div class="abs front-contact phone-line">
    <svg width="16" height="16" viewBox="0 0 16 16"><path d="M4 1.5l2.3 3-1.3 1.6c.8 1.8 2.2 3.2 4 4l1.6-1.3 3 2.3-1.4 2.2C7 13.2 2.8 9 2 4z" fill="#fff"/></svg>
    555-240-3180
  </div>
  <div class="abs front-contact web-line">
    <svg width="14" height="14" viewBox="0 0 14 14"><circle cx="7" cy="7" r="6" fill="none" stroke="#fff"/><ellipse cx="7" cy="7" rx="2.6" ry="6" fill="none" stroke="#fff" stroke-width=".8"/><path d="M1 7h12" stroke="#fff" stroke-width=".8"/></svg>
    www.<em>pineridgegolf</em>.com
  </div>
</section>

<!-- BACK -->
<section class="postcard postcard--back back">
  <svg class="backdrop" width="680" height="522" viewBox="0 0 680 522">
    <defs>
      <linearGradient id="darkScene" x1="0" y1="0" x2="0" y2="1">
        <stop offset="0" stop-color="#1d1d1d"/>
        <stop offset=".5" stop-color="#3a3a36"/>
        <stop offset="1" stop-color="#4a5a3a"/>
      </linearGradient>
      <linearGradient id="greyBand" x1="0" y1="0" x2="1" y2="0">
        <stop offset="0" stop-color="#bdbdbd"/><stop offset=".5" stop-color="#f2f2f2"/><stop offset="1" stop-color="#9e9e9e"/>
      </linearGradient>
    </defs>
    <path d="M248 0 C360 40 425 190 375 320 L338 434 L0 434 L0 0 Z" fill="none" stroke="#bcbcbc" stroke-width="30"/>
    <path d="M248 0 C360 40 425 190 375 320 L338 434" fill="none" stroke="var(--red)" stroke-width="18"/>
    <path d="M248 0 C360 40 425 190 375 320 L338 434 L0 434 L0 0 Z" fill="url(#darkScene)" role="img" aria-label="Close-up of a golf ball on a tee at dusk"/>
    <polygon points="0,402 349,402 338,434 0,434" fill="url(#greyBand)"/>
  </svg>

  <span class="abs sign-cord" style="left:42px"></span>
  <span class="abs sign-cord" style="left:235px"></span>
  <div class="abs call-sign">
    <div class="call-sign__title">CALL NOW</div>
    <div class="call-sign__sub">For a tour or to sign up</div>
    <div class="call-sign__phone">
      <svg width="16" height="16" viewBox="0 0 16 16"><path d="M4 1.5l2.3 3-1.3 1.6c.8 1.8 2.2 3.2 4 4l1.6-1.3 3 2.3-1.4 2.2C7 13.2 2.8 9 2 4z" fill="#fff"/></svg>
      555-240-3180
    </div>
    <div class="call-sign__mail">
      <svg width="16" height="16" viewBox="0 0 16 16"><circle cx="8" cy="8" r="7" fill="none" stroke="#fff"/><rect x="4" y="5.5" width="8" height="5.5" fill="none" stroke="#fff" stroke-width=".9"/><path d="M4 5.5l4 3 4-3" fill="none" stroke="#fff" stroke-width=".9"/></svg>
      info@pineridgegolf.com
    </div>
    <div class="call-sign__foot">LIMITED MEMBERSHIPS AVAILABLE.</div>
  </div>

  <div class="abs location-map" role="img" aria-label="Street map showing the facility location"></div>

  <div class="abs web-back">
    <svg width="16" height="16" viewBox="0 0 16 16"><circle cx="8" cy="8" r="7" fill="var(--red)" stroke="#555"/><ellipse cx="8" cy="8" rx="3" ry="6.5" fill="none" stroke="#fff" stroke-width=".8"/><path d="M1.5 8h13" stroke="#fff" stroke-width=".8"/></svg>
    <span>www.<em>pineridgegolf</em>.com</span>
  </div>

  <div class="brand">
    <div class="brand__name">Pine Ridge Golf</div>
    <div class="brand__tag">Indoor golf training center</div>
  </div>

  <div class="abs stamp-box"></div>
  <span class="abs address-line" style="top:286px"></span>
  <span class="abs address-line" style="top:332px"></span>
  <span class="abs address-line" style="top:379px"></span>
</section>

</body>
</html>
```